WEBSITE NEEDED FOR MY COMPANY CALLED BRAVLON HOCKEY DEVELOPMENT

LOOKING FOR A WEBSITE TO MARKET AND SEEL MY HOCKEY DEVELOPMENT PROGRAMS.
NEEDS TO HAVE 5+ PAGES

Target Market(s)

YOUTH SPORTS

Industry/Entity Type

YOUTH ATHLETE DEVELOPMENT

Number of Pages Required

5+ page

Font styles to use
Sans Serif

Colors
0054AA
0677BA
7BADD7
CADEEF
E8F1F8

Requirements
Must have
• MAIN PAGE - SPIRNG PROGRAM PAGE - SUMMER PROGRAM PAGE - WINTER PAGE - TOURNAMENT PAGE
Nice to have
• FLASH
Should not have
• NOT SURE

```html
<!DOCTYPE html>
<html lang="en">
<head>
<meta charset="utf-8">
<title>Bravlon Hockey Development</title>
<link href="https://fonts.googleapis.com/css2?family=Exo+2:ital,wght@0,700;1,800;1,900&family=Poppins:wght@400;500;600;700;800&display=swap" rel="stylesheet">
<style>
:root{
  --navy:#0b1d38;
  --navy-deep:#071328;
  --cyan:#22b4ec;
  --blue:#0677ba;
  --royal:#0054aa;
  --ice:#e8f1f8;
  --mist:#cadeef;
  --sky:#7badd7;
  --ink:#1a1f2b;
  --white:#ffffff;
}
*{box-sizing:border-box;margin:0;padding:0}
html,body{width:1200px;height:4780px;overflow:hidden;background:var(--white)}
body{font-family:"Poppins",sans-serif;color:var(--ink);position:relative}
.abs{position:absolute}
.display{font-family:"Exo 2",sans-serif;font-style:italic;font-weight:900;letter-spacing:2px;text-transform:uppercase}
.accent{color:var(--cyan)}
.dark{color:var(--navy)}
.btn{display:inline-block;border-radius:30px;font-family:"Exo 2",sans-serif;font-weight:700;font-style:italic;text-transform:uppercase;letter-spacing:1px;color:var(--white);font-size:17px;padding:12px 30px}
.btn-cyan{background:var(--cyan)}
.btn-navy{background:var(--navy)}
.photo{position:absolute}

/* hero */
.hero{position:absolute;left:0;top:0;width:1200px;height:900px;overflow:hidden}
.hero-photo{position:absolute;inset:0;background:radial-gradient(circle at 62% 30%,#5d7fa6 0%,#27476f 35%,#0f2442 70%,#081527 100%)}
.brand{position:absolute;left:40px;top:24px;display:flex;align-items:center;gap:14px;font-family:"Poppins",sans-serif;font-weight:800;color:var(--white);font-size:30px;line-height:1.05}
.brand .mark{width:22px;height:22px;border-radius:50%;background:var(--cyan)}
.phone{position:absolute;right:40px;top:22px;display:flex;align-items:center;gap:10px;color:var(--cyan);font-family:"Exo 2",sans-serif;font-style:italic;font-weight:800;font-size:24px}
.nav{position:absolute;right:40px;top:72px;display:flex;gap:30px;font-size:15px;font-weight:600;text-transform:uppercase;color:var(--white)}
.nav .current{color:var(--cyan)}
.hero-title{position:absolute;left:90px;top:250px;color:var(--white);font-size:104px;line-height:.95}
.hero-sub{position:absolute;left:94px;top:470px;color:var(--mist);font-family:"Exo 2",sans-serif;font-weight:700;font-size:44px;line-height:1.05;letter-spacing:2px;text-transform:uppercase}
.hero .btn{position:absolute;left:96px;top:570px}

/* about */
.section-title{font-size:64px;line-height:1}
.about-title{left:100px;top:985px}
.about-text{left:100px;top:1080px;width:450px;font-size:18px;line-height:1.55;font-weight:500;color:#2a2f3a}
.about .btn{left:100px;top:1290px}

/* programs */
.programs-title{left:0;top:1600px;width:1200px;text-align:center;color:var(--white)}
.program{position:absolute;top:1750px;width:300px;text-align:center;color:var(--white)}
.program .frame{position:absolute;left:-14px;top:-14px;width:300px;height:290px;border:4px solid var(--cyan);border-radius:6px}
.program .pic{position:relative;height:290px;border-radius:6px}
.program .date{margin-top:28px;font-size:17px;font-weight:500}
.program h3{font-size:26px;font-weight:700;text-transform:uppercase;letter-spacing:1px;margin-top:4px}
.program p{font-size:15px;line-height:1.4;color:var(--mist);margin:8px 14px 0}
.program .go{margin:16px auto 0;width:44px;height:44px;border-radius:50%;background:var(--cyan);display:flex;align-items:center;justify-content:center}
.slider-arrow{position:absolute;width:48px;height:48px;border-radius:50%;border:2px solid #5d6c82;display:flex;align-items:center;justify-content:center}

/* team */
.team-title{left:100px;top:2520px}
.team-text{left:100px;top:2625px;width:400px;font-size:16px;line-height:1.5;color:#2a2f3a}
.team .btn{left:100px;top:2770px}

/* events */
.events-title{left:495px;top:3160px;color:var(--white);font-size:60px}
.events-lead{left:495px;top:3245px;width:600px;color:var(--white);font-weight:700;font-size:26px;line-height:1.35}
.events-text{left:495px;top:3345px;width:600px;color:var(--white);font-size:17px;line-height:1.5}
.events-date{left:495px;top:3455px;display:flex;align-items:center;gap:16px;color:var(--white);font-family:"Exo 2",sans-serif;font-weight:700;font-size:34px}

/* news */
.news-title{left:0;top:3695px;width:1200px;text-align:center}
.news-card{position:absolute;top:3820px;width:310px;height:370px;background:var(--white);box-shadow:0 6px 22px rgba(10,30,60,.22)}
.news-card .pic{height:190px}
.news-card h4{margin:20px 22px 0;font-size:17px;font-weight:700;line-height:1.3}
.news-card p{margin:8px 22px 0;font-size:13px;line-height:1.45;color:#4a5161}
.news-card .date{margin:14px 22px 0;display:flex;align-items:center;gap:10px;font-size:13px;color:#4a5161}

/* footer */
.footer-brand{left:110px;top:4550px;font-size:40px}
.socials{left:130px;top:4680px;display:flex;gap:24px}
.socials span{width:22px;height:22px;border-radius:50%;border:2px solid var(--cyan)}
.foot-col{position:absolute;top:4510px;color:var(--white)}
.foot-col h5{font-family:"Exo 2",sans-serif;font-weight:700;font-size:24px;text-transform:uppercase;letter-spacing:1px;margin-bottom:18px}
.foot-col li{list-style:none;font-size:15px;line-height:1.8;color:var(--mist)}
.contact-row{display:flex;gap:14px;align-items:flex-start;font-size:14px;line-height:1.4;color:var(--mist);margin-bottom:16px;width:230px}
.contact-row i{flex:none;width:30px;height:30px;border-radius:50%;background:var(--cyan)}
.field{width:200px;height:30px;background:var(--white);border-radius:3px;margin-bottom:10px;font-size:12px;color:#8a93a3;padding:6px 10px}
.submit{display:inline-block;background:var(--cyan);color:var(--white);font-size:12px;font-weight:700;text-transform:uppercase;padding:6px 20px;border-radius:3px}
.copyright{left:0;top:4745px;width:1200px;text-align:center;font-size:13px;color:var(--sky);text-transform:uppercase;letter-spacing:1px}
</style>
</head>
<body>

<!-- HERO -->
<header class="hero">
  <div class="hero-photo" role="img" aria-label="Photo of two youth hockey players battling for the puck on an arena rink"></div>
  <svg class="abs" style="left:0;top:0" width="1200" height="900" viewBox="0 0 1200 900">
    <path d="M0 700 C 300 840, 700 880, 1200 660 L1200 900 L0 900 Z" fill="var(--cyan)"/>
    <path d="M0 740 C 320 880, 720 900, 1200 720 L1200 900 L0 900 Z" fill="var(--white)"/>
  </svg>
  <div class="brand"><span class="mark"></span><span>BRAVLON<br>HOCKEY<br>DEVELOPMENT</span></div>
  <div class="phone">
    <svg width="22" height="22" viewBox="0 0 24 24"><path d="M6.6 10.8a15 15 0 0 0 6.6 6.6l2.2-2.2a1 1 0 0 1 1-.25 11 11 0 0 0 3.6.6 1 1 0 0 1 1 1V20a1 1 0 0 1-1 1A17 17 0 0 1 3 4a1 1 0 0 1 1-1h3.5a1 1 0 0 1 1 1 11 11 0 0 0 .6 3.6 1 1 0 0 1-.25 1z" fill="var(--cyan)"/></svg>
    Call Us: 555 014 2290
  </div>
  <nav class="nav">
    <span class="current">Home</span><span>Spring Programme</span><span>Summer Programme</span><span>Winter Programme</span><span>Tournament</span>
  </nav>
  <h1 class="hero-title display">Bravlon<br>Hockey</h1>
  <div class="hero-sub">Hockey Development<br>Programs.</div>
  <a class="btn btn-cyan">Learn More</a>
</header>

<!-- ABOUT -->
<section class="about">
  <svg class="abs" style="left:620px;top:800px" width="520" height="520" viewBox="0 0 520 520" role="img" aria-label="Photo of a young hockey player skating with the puck in an arena">
    <defs>
      <linearGradient id="aboutPhoto" x1="0" y1="0" x2="0" y2="1">
        <stop offset="0" stop-color="#2c4466"/><stop offset=".55" stop-color="#6f8aa8"/><stop offset="1" stop-color="#dfe8f1"/>
      </linearGradient>
    </defs>
    <path d="M470 20 L470 270 A215 215 0 1 1 255 55 Z" fill="var(--cyan)"/>
    <path d="M450 40 L450 275 A200 200 0 1 1 250 75 Z" fill="var(--white)"/>
    <path d="M440 50 L440 275 A190 190 0 1 1 250 85 Z" fill="url(#aboutPhoto)"/>
  </svg>
  <h2 class="abs section-title display about-title"><span class="accent">About</span> <span class="dark">Us</span></h2>
  <p class="abs about-text">Lorem ipsum dolor sit amet, consectetur adipiscing elit, sed do eiusmod tempor incididunt ut labore et dolore magna aliqua. Ut enim ad minim veniam, quis nostrud exercitation ullamco laboris nisi ut aliquip ex ea commodo consequat. Duis aute irure dolor in reprehenderit in voluptate velit esse cillum dolore eu fugiat nulla pariatur.</p>
  <a class="abs btn btn-navy">Read More</a>
</section>

<!-- PROGRAMS -->
<section class="programs">
  <svg class="abs" style="left:0;top:1440px" width="1200" height="1000" viewBox="0 0 1200 1000">
    <path d="M0 120 C 300 20, 700 140, 1200 60 L1200 900 C 800 990, 400 860, 0 930 Z" fill="var(--navy)"/>
    <path d="M820 70 C 960 50, 1080 50, 1200 30 L1200 60 C 1080 90, 960 90, 820 70 Z" fill="var(--blue)"/>
    <path d="M0 930 C 200 895, 330 880, 470 890 C 330 905, 180 925, 0 960 Z" fill="var(--blue)"/>
  </svg>
  <h2 class="abs section-title display programs-title">Our <span class="accent">Programs</span></h2>

  <div class="slider-arrow" style="left:22px;top:1890px"><svg width="16" height="16" viewBox="0 0 16 16"><path d="M10 2 L4 8 L10 14" stroke="#8a99ae" stroke-width="2.5" fill="none"/></svg></div>
  <div class="slider-arrow" style="left:1130px;top:1890px"><svg width="16" height="16" viewBox="0 0 16 16"><path d="M6 2 L12 8 L6 14" stroke="#8a99ae" stroke-width="2.5" fill="none"/></svg></div>

  <article class="program" style="left:120px">
    <div class="frame"></div>
    <div class="pic" role="img" aria-label="Photo of a hockey player spraying ice while stopping" style="background:linear-gradient(160deg,#a7b7c6,#5a6b7c 60%,#2a3646)"></div>
    <div class="date">02.07.2022</div>
    <h3>Summer Program</h3>
    <p>Lorem ipsum dolor sit amet, eiusmod tempor incididunt ut magna aliqua.</p>
    <div class="go"><svg width="20" height="20" viewBox="0 0 20 20"><path d="M3 10 H16 M11 5 L16 10 L11 15" stroke="#fff" stroke-width="3" fill="none"/></svg></div>
  </article>
  <article class="program" style="left:450px">
    <div class="frame"></div>
    <div class="pic" role="img" aria-label="Photo of a youth hockey player handling the puck" style="background:linear-gradient(160deg,#6f86a3,#2f4a6e 55%,#14243c)"></div>
    <div class="date">12.07.2022</div>
    <h3>Summer Program</h3>
    <p>Lorem ipsum dolor sit amet, eiusmod tempor incididunt ut magna aliqua.</p>
    <div class="go"><svg width="20" height="20" viewBox="0 0 20 20"><path d="M3 10 H16 M11 5 L16 10 L11 15" stroke="#fff" stroke-width="3" fill="none"/></svg></div>
  </article>
  <article class="program" style="left:780px">
    <div class="frame"></div>
    <div class="pic" role="img" aria-label="Photo of hockey players on a rink under arena lights" style="background:linear-gradient(160deg,#8fa8c4,#41597a 50%,#1b2a42)"></div>
    <div class="date">22.07.2022</div>
    <h3>Summer Program</h3>
    <p>Lorem ipsum dolor sit amet, eiusmod tempor incididunt ut magna aliqua.</p>
    <div class="go"><svg width="20" height="20" viewBox="0 0 20 20"><path d="M3 10 H16 M11 5 L16 10 L11 15" stroke="#fff" stroke-width="3" fill="none"/></svg></div>
  </article>
</section>

<!-- TEAM -->
<section class="team">
  <h2 class="abs section-title display team-title"><span class="accent">Our</span> <span class="dark">Team</span></h2>
  <p class="abs team-text">Lorem ipsum dolor sit amet, consectetur adipiscing elit, sed do eiusmod tempor incididunt ut labore et dolore magna aliqua. Ut enim ad minim veniam, quis nostrud exercitation ullamco laboris nisi ut aliquip ex ea commodo consequat.</p>
  <a class="abs btn btn-navy">View More</a>
  <svg class="abs" style="left:510px;top:2470px" width="610" height="440" viewBox="0 0 610 440" role="img" aria-label="Photo of a youth hockey team in blue jerseys posing on the ice">
    <defs>
      <linearGradient id="teamPhoto" x1="0" y1="0" x2="0" y2="1">
        <stop offset="0" stop-color="#1a2330"/><stop offset=".5" stop-color="#2c5a9a"/><stop offset="1" stop-color="#c9d6e3"/>
      </linearGradient>
    </defs>
    <path d="M20 20 L600 0 L590 390 L0 440 Z" fill="url(#teamPhoto)"/>
  </svg>
</section>

<!-- EVENTS -->
<section class="events">
  <svg class="abs" style="left:0;top:2960px" width="1200" height="700" viewBox="0 0 1200 700">
    <path d="M0 90 C 300 0, 800 10, 1200 60 L1200 660 C 800 560, 300 620, 0 690 Z" fill="var(--cyan)"/>
    <path d="M0 90 C 300 0, 800 10, 1200 60 L1200 20 C 800 -20, 300 -30, 0 50 Z" fill="var(--navy)"/>
    <path d="M560 20 C 800 30, 1000 70, 1200 120 L1200 160 C 1000 100, 800 60, 560 20 Z" fill="var(--royal)" opacity=".55"/>
    <path d="M0 690 C 300 620, 800 560, 1200 660 L1200 700 L0 700 Z" fill="var(--white)"/>
    <path d="M700 600 C 900 585, 1050 610, 1200 640 L1200 660 C 1050 630, 900 605, 700 600 Z" fill="var(--navy)"/>
  </svg>
  <div class="photo" role="img" aria-label="Cut-out photo of a hockey player in a red jersey skating with his stick" style="left:130px;top:2990px;width:320px;height:580px;border-radius:140px 140px 40px 40px;background:linear-gradient(180deg,#3b2b2e,#b52a32 35%,#c93b40 55%,#2a2d36 80%,#d8dde3)"></div>
  <h2 class="abs display events-title">Latest Events</h2>
  <p class="abs events-lead">Lorem ipsum dolor sit amet, consectetur adipiscing elit, sed do eiusmod tempor</p>
  <p class="abs events-text">Lorem ipsum dolor sit amet, consectetur adipiscing elit, sed do eiusmod tempor incididunt ut labore et dolore magna aliqua. Ut enim ad minim veniam, quis nostrud.</p>
  <div class="abs events-date">
    <svg width="42" height="42" viewBox="0 0 24 24"><rect x="3" y="5" width="18" height="16" rx="2" fill="none" stroke="#fff" stroke-width="2"/><path d="M3 10 H21 M8 3 V7 M16 3 V7" stroke="#fff" stroke-width="2"/><rect x="7" y="13" width="3" height="3" fill="#fff"/><rect x="14" y="13" width="3" height="3" fill="#fff"/></svg>
    12.06.2022
  </div>
</section>

<!-- NEWS -->
<section class="news">
  <h2 class="abs section-title display news-title"><span class="accent">Latest</span> <span class="dark">News</span></h2>
  <div class="slider-arrow" style="left:22px;top:3970px;border-color:#b6bfcc"><svg width="16" height="16" viewBox="0 0 16 16"><path d="M10 2 L4 8 L10 14" stroke="#9aa5b5" stroke-width="2.5" fill="none"/></svg></div>
  <div class="slider-arrow" style="left:1130px;top:3970px;border-color:#b6bfcc"><svg width="16" height="16" viewBox="0 0 16 16"><path d="M6 2 L12 8 L6 14" stroke="#9aa5b5" stroke-width="2.5" fill="none"/></svg></div>

  <article class="news-card" style="left:100px">
    <div class="pic" role="img" aria-label="Photo of youth players chasing the puck in a game" style="background:linear-gradient(160deg,#6b84a6,#2a4470 60%,#c4d2e0)"></div>
    <h4>Lorem ipsum dolor sit amet, consectetur</h4>
    <p>Lorem ipsum dolor sit amet, consectetur adipiscing elit sed do eiusmod tempor.</p>
    <div class="date"><svg width="18" height="18" viewBox="0 0 24 24"><rect x="3" y="5" width="18" height="16" rx="2" fill="var(--cyan)"/><rect x="5" y="10" width="14" height="9" fill="#fff"/></svg>12.06.2022</div>
  </article>
  <article class="news-card" style="left:445px">
    <div class="pic" role="img" aria-label="Photo of players lined up during a hockey practice drill" style="background:linear-gradient(160deg,#8797ab,#4b5f7a 55%,#dfe6ee)"></div>
    <h4>Lorem ipsum dolor sit amet, consectetur</h4>
    <p>Lorem ipsum dolor sit amet, consectetur adipiscing elit sed do eiusmod tempor.</p>
    <div class="date"><svg width="18" height="18" viewBox="0 0 24 24"><rect x="3" y="5" width="18" height="16" rx="2" fill="var(--cyan)"/><rect x="5" y="10" width="14" height="9" fill="#fff"/></svg>12.06.2022</div>
  </article>
  <article class="news-card" style="left:790px">
    <div class="pic" role="img" aria-label="Photo of a goalie and players near the net" style="background:linear-gradient(160deg,#2d3f5a,#35618f 55%,#cbd8e6)"></div>
    <h4>Lorem ipsum dolor sit amet, consectetur</h4>
    <p>Lorem ipsum dolor sit amet, consectetur adipiscing elit sed do eiusmod tempor.</p>
    <div class="date"><svg width="18" height="18" viewBox="0 0 24 24"><rect x="3" y="5" width="18" height="16" rx="2" fill="var(--cyan)"/><rect x="5" y="10" width="14" height="9" fill="#fff"/></svg>12.06.2022</div>
  </article>
</section>

<!-- FOOTER -->
<footer class="footer">
  <svg class="abs" style="left:0;top:4320px" width="1200" height="460" viewBox="0 0 1200 460">
    <path d="M0 90 C 350 10, 800 10, 1200 70 L1200 460 L0 460 Z" fill="var(--navy)"/>
    <path d="M0 90 C 350 10, 800 10, 1200 70 L1200 50 C 800 -10, 350 -10, 0 70 Z" fill="var(--cyan)"/>
    <line x1="0" y1="405" x2="1200" y2="405" stroke="#23395a" stroke-width="1"/>
  </svg>
  <div class="abs brand footer-brand" style="position:absolute"><span class="mark"></span><span>BRAVLON<br>HOCKEY</span></div>
  <div class="abs socials"><span></span><span></span><span></span></div>

  <div class="foot-col" style="left:440px">
    <h5>Quick Links</h5>
    <ul><li>Home</li><li>Spring Program</li><li>Summer Program</li><li>Winter Program</li><li>Tournament</li></ul>
  </div>
  <div class="foot-col" style="left:660px">
    <h5>Contact Us</h5>
    <div class="contact-row"><i></i><span>42 Rinkside Way, Suite 8, Northgate</span></div>
    <div class="contact-row"><i></i><span>555 014 2290</span></div>
    <div class="contact-row"><i></i><span>hello@bravlonhockey.com</span></div>
  </div>
  <div class="foot-col" style="left:910px">
    <h5>Get In Touch</h5>
    <div class="field">Name</div>
    <div class="field">Email</div>
    <div class="field">Message</div>
    <span class="submit">Submit</span>
  </div>
  <div class="abs copyright">Copyright © 2021 Bravlon Hockey. All rights reserved</div>
</footer>

</body>
</html>
```